PowerPoint design MedoraVix

We need a PowerPoint set-up based upon our existing logo (see joint file)
Our company is operating in the health care and life science sector. We are mainly focussing on international business

Target Market(s)

International

Industry/Entity Type

health care and life sciences

Requirements
Must have
• Logos as added

```html
<!DOCTYPE html>
<html lang="en">
<head>
<meta charset="utf-8">
<title>MedoraVix – Presentation Set</title>
<link rel="stylesheet" href="https://fonts.googleapis.com/css2?family=Quicksand:wght@600;700&family=Roboto:wght@400;500;700&family=Oswald:wght@600&display=swap">
<style>
  :root{
    --navy:#0b3a75;
    --navy-deep:#082e5e;
    --green:#4cb80f;
    --green-light:#7fd23c;
    --white:#ffffff;
    --ink:#1d1d1f;
    --muted:#5a5a5a;
    --canvas:#9a9b9d;
    --grid:#d9dde3;
  }
  *{box-sizing:border-box;margin:0;padding:0}
  html,body{width:1200px;height:3916px;overflow:hidden}
  body{background:var(--canvas);position:relative;font-family:"Roboto",Arial,sans-serif;color:var(--ink)}
  .slide{position:absolute;width:981px;height:552px;overflow:hidden;background:var(--white)}
  .abs{position:absolute}
  .slide-title{position:absolute;font-family:"Quicksand",sans-serif;font-weight:700;font-size:45px;color:var(--white);line-height:1;transform:translateY(-50%)}
  .brand{position:absolute;display:flex;align-items:center;gap:10px;transform:translateY(-50%)}
  .brand-dot{width:38px;height:38px;border-radius:50%;background:var(--white)}
  .brand-name{font-family:"Quicksand",sans-serif;font-weight:700;font-size:27px;color:var(--white)}
  .brand.on-white .brand-dot{background:var(--navy)}
  .brand.on-white .brand-name{color:var(--navy)}
  .photo{position:absolute}

  /* cover */
  .cover{left:114px;top:113px;background:var(--navy)}
  .cover .photo{inset:0;background:
      radial-gradient(circle at 75% 50%, rgba(110,210,70,.75) 0, rgba(60,150,120,.45) 22%, rgba(11,58,117,0) 48%),
      radial-gradient(circle at 60% 40%, rgba(170,140,220,.35) 0, rgba(11,58,117,0) 30%),
      linear-gradient(120deg,#123f86 0%,#0d3a7c 45%,#164c8e 100%)}
  .cover-title{position:absolute;left:58px;top:275px;transform:translateY(-50%);font-family:"Quicksand",sans-serif;font-weight:700;font-size:72px;color:var(--white);line-height:1}
  .cover-sub{position:absolute;left:60px;top:333px;transform:translateY(-50%);font-family:"Roboto",sans-serif;font-weight:500;font-size:30px;color:var(--white)}

  /* vision / mission */
  .vision{left:114px;top:741px}
  .vm-icon{position:absolute;width:76px;height:76px;border-radius:50%;transform:translate(-50%,-50%);display:flex;align-items:center;justify-content:center}
  .vm-head{position:absolute;left:155px;font-weight:700;font-size:14px;color:var(--ink)}
  .vm-body{position:absolute;left:155px;width:300px;font-size:12px;line-height:19px;color:var(--muted)}
  .vision .photo{left:509px;top:176px;width:411px;height:315px;border-radius:26px;background:linear-gradient(135deg,#2a2f36 0%,#3f6c8c 35%,#6aa7c4 55%,#1f2a33 100%)}

  /* bullets */
  .bullets{left:114px;top:1369px;background:var(--green)}
  .tick-list{position:absolute;left:61px;top:130px;list-style:none;width:430px}
  .tick-list li{position:relative;padding-left:23px;font-size:12px;line-height:19px;color:var(--white);height:47px}
  .tick{position:absolute;left:0;top:3px;width:12px;height:12px}
  .bullets .photo{left:544px;top:99px;width:377px;height:392px;border-radius:40px 40px 0 40px;background:radial-gradient(circle at 45% 45%,#d9eefa 0,#8bbfe0 35%,#3e79a8 70%,#1f4f7c 100%)}

  /* puzzle */
  .puzzle{left:105px;top:1997px}
  .pz-head{position:absolute;font-weight:700;font-size:12.5px;color:var(--ink);white-space:nowrap}
  .pz-body{position:absolute;width:272px;font-size:11.5px;line-height:21px;color:var(--muted)}
  .pz-left{text-align:right}

  /* growth */
  .growth{left:114px;top:2625px;background:var(--green)}
  .growth-title{position:absolute;left:24px;top:264px;transform:translateY(-50%);font-family:"Quicksand",sans-serif;font-weight:700;font-size:40px;color:var(--white)}
  .growth-rule{position:absolute;left:24px;top:295px;width:82px;height:5px;background:var(--navy)}
  .growth-list{position:absolute;left:701px;top:72px;list-style:none;width:240px}
  .growth-list li{position:relative;padding-left:19px;font-size:11px;line-height:19.5px;color:var(--muted);height:70px}
  .growth-list .tick{left:0;top:4px;width:11px;height:11px}

  /* closing */
  .closing{left:110px;top:3253px}
  .closing .photo{inset:0;background:linear-gradient(135deg,#c9ccd2 0%,#8d99ab 40%,#4b5c78 75%,#33415a 100%)}
  .thanks-dash{position:absolute;left:660px;top:178px;display:flex;gap:5px}
  .thanks-dash span{width:9px;height:5px;background:var(--green);border-radius:2px}
  .thanks{position:absolute;left:660px;top:219px;transform:translateY(-50%);font-family:"Oswald",sans-serif;font-weight:600;font-size:44px;color:var(--navy);letter-spacing:.5px;line-height:1}
  .presenter{position:absolute;left:665px;top:317px;transform:translateY(-50%);font-weight:700;font-size:23px;color:var(--green)}
  .contact{position:absolute;left:665px;display:flex;align-items:center;gap:14px;transform:translateY(-50%);font-weight:700;font-size:14px;color:var(--navy)}
  .contact svg{width:28px;height:28px}
</style>
</head>
<body>

<!-- Cover -->
<section class="slide cover">
  <div class="photo" role="img" aria-label="Blue-toned life science photograph of a DNA strand and cells with a green glow on the right"></div>
  <div class="brand" style="left:61px;top:53px"><span class="brand-dot"></span><span class="brand-name">MedoraVix</span></div>
  <h1 class="cover-title">MedoraVix</h1>
  <p class="cover-sub">Global Health Partners</p>
</section>

<!-- Vision & Mission -->
<section class="slide vision">
  <svg class="abs" width="981" height="552" style="left:0;top:0">
    <rect width="981" height="552" fill="var(--green)"/>
    <path d="M0,200 C0,140 50,110 120,110 L870,110 C940,110 981,70 981,20 L981,552 L0,552 Z" fill="var(--white)"/>
  </svg>
  <h2 class="slide-title" style="left:61px;top:53px">Title Here</h2>
  <div class="brand" style="left:732px;top:53px"><span class="brand-dot"></span><span class="brand-name">MedoraVix</span></div>

  <div class="vm-icon" style="left:99px;top:252px;background:var(--navy)">
    <svg width="38" height="38" viewBox="0 0 38 38" fill="none" stroke="#fff" stroke-width="2"><circle cx="19" cy="19" r="15"/><circle cx="19" cy="19" r="9"/><circle cx="19" cy="19" r="3"/></svg>
  </div>
  <h3 class="vm-head" style="top:218px">Vision</h3>
  <p class="vm-body" style="top:238px">At vero eos et accusamus et iusto dignissimos ducimus qui blanditiis praesentium voluptatum deleniti atque corrupti</p>

  <div class="vm-icon" style="left:99px;top:380px;background:var(--green)">
    <svg width="38" height="38" viewBox="0 0 38 38" fill="none" stroke="#fff" stroke-width="2" stroke-linecap="round"><path d="M8 16 L28 8 L31 15 L11 23 Z"/><path d="M19 19 L13 33 M19 19 L25 33 M19 19 V33"/></svg>
  </div>
  <h3 class="vm-head" style="top:346px">Mission</h3>
  <p class="vm-body" style="top:366px">Sed ut perspiciatis unde omnis iste natus error sit voluptatem accusantium doloremque laudantium, totam rem aperiam, eaque ipsa quae ab illo inventore veritatis et quasi</p>

  <div class="photo" role="img" aria-label="Tablet showing a doctor with digital health icons"></div>
</section>

<!-- Bullet list -->
<section class="slide bullets">
  <svg class="abs" width="981" height="552" style="left:0;top:0">
    <path d="M0,0 H715 C765,0 787,40 787,100 V552 H0 Z" fill="var(--white)"/>
    <path d="M0,0 H700 C750,0 775,40 775,100 V552 H0 Z" fill="var(--navy)"/>
  </svg>
  <h2 class="slide-title" style="left:61px;top:53px">Title Here</h2>
  <ul class="tick-list">
    <li><svg class="tick" viewBox="0 0 12 12"><circle cx="6" cy="6" r="6" fill="var(--green)"/><path d="M3.2 6.2 L5.2 8 L8.8 4.2" stroke="#fff" stroke-width="1.5" fill="none"/></svg>Lorem ipsum dolor sit consectetur adipiscing elit, sed do eiusmod tempor incididunt ut labore et dolore magna aliqua.</li>
    <li><svg class="tick" viewBox="0 0 12 12"><circle cx="6" cy="6" r="6" fill="var(--green)"/><path d="M3.2 6.2 L5.2 8 L8.8 4.2" stroke="#fff" stroke-width="1.5" fill="none"/></svg>Lorem ipsum dolor sit consectetur adipiscing elit, sed do eiusmod tempor incididunt ut labore et dolore magna aliqua.</li>
    <li><svg class="tick" viewBox="0 0 12 12"><circle cx="6" cy="6" r="6" fill="var(--green)"/><path d="M3.2 6.2 L5.2 8 L8.8 4.2" stroke="#fff" stroke-width="1.5" fill="none"/></svg>Lorem ipsum dolor sit consectetur adipiscing elit, sed do eiusmod tempor incididunt ut labore et dolore magna aliqua.</li>
    <li><svg class="tick" viewBox="0 0 12 12"><circle cx="6" cy="6" r="6" fill="var(--green)"/><path d="M3.2 6.2 L5.2 8 L8.8 4.2" stroke="#fff" stroke-width="1.5" fill="none"/></svg>Lorem ipsum dolor sit consectetur adipiscing elit, sed do eiusmod tempor incididunt ut labore et dolore magna aliqua.</li>
    <li><svg class="tick" viewBox="0 0 12 12"><circle cx="6" cy="6" r="6" fill="var(--green)"/><path d="M3.2 6.2 L5.2 8 L8.8 4.2" stroke="#fff" stroke-width="1.5" fill="none"/></svg>Lorem ipsum dolor sit consectetur adipiscing elit, sed do eiusmod tempor incididunt ut labore et dolore magna aliqua.</li>
    <li><svg class="tick" viewBox="0 0 12 12"><circle cx="6" cy="6" r="6" fill="var(--green)"/><path d="M3.2 6.2 L5.2 8 L8.8 4.2" stroke="#fff" stroke-width="1.5" fill="none"/></svg>Lorem ipsum dolor sit consectetur adipiscing elit, sed do eiusmod tempor incididunt ut labore et dolore magna aliqua.</li>
    <li><svg class="tick" viewBox="0 0 12 12"><circle cx="6" cy="6" r="6" fill="var(--green)"/><path d="M3.2 6.2 L5.2 8 L8.8 4.2" stroke="#fff" stroke-width="1.5" fill="none"/></svg>Lorem ipsum dolor sit consectetur adipiscing elit, sed do eiusmod tempor incididunt ut labore et dolore magna aliqua.</li>
  </ul>
  <div class="photo" role="img" aria-label="Open hand holding glowing medical icons"></div>
</section>

<!-- Four-part diagram -->
<section class="slide puzzle">
  <svg class="abs" width="981" height="552" style="left:0;top:0">
    <rect width="981" height="552" fill="var(--navy)"/>
    <path d="M0,200 C0,140 50,110 120,110 L870,110 C940,110 981,70 981,20 L981,552 L0,552 Z" fill="var(--white)"/>
    <g transform="translate(491,330)">
      <path d="M0,0 L0,-147 A147,147 0 0,0 -147,0 Z" fill="var(--green)"/>
      <path d="M0,0 L147,0 A147,147 0 0,0 0,-147 Z" fill="var(--navy)"/>
      <path d="M0,0 L-147,0 A147,147 0 0,0 0,147 Z" fill="var(--navy)"/>
      <path d="M0,0 L0,147 A147,147 0 0,0 147,0 Z" fill="var(--green)"/>
      <circle cx="22" cy="-100" r="13" fill="var(--green)"/>
      <circle cx="100" cy="22" r="13" fill="var(--green)"/>
      <circle cx="-22" cy="100" r="13" fill="var(--green)"/>
      <circle cx="-100" cy="-22" r="13" fill="var(--navy)"/>
      <path d="M0,-150 V150 M-150,0 H150" stroke="#fff" stroke-width="7"/>
      <circle r="62" fill="#fff"/>
      <circle r="46" fill="#fff" stroke="var(--navy)" stroke-width="5"/>
    </g>
  </svg>
  <h2 class="slide-title" style="left:61px;top:53px">Title Here</h2>
  <div class="brand" style="left:732px;top:53px"><span class="brand-dot"></span><span class="brand-name">MedoraVix</span></div>

  <h3 class="pz-head" style="right:648px;top:176px">Lorem ipsum dolor sit consectetur</h3>
  <p class="pz-body pz-left" style="left:61px;top:207px">Sed ut perspiciatis unde omnis iste natus error sit voluptatem accusantium doloremque laudantium, totam rem aperiam, eaque</p>
  <h3 class="pz-head" style="right:648px;top:380px">Lorem ipsum dolor sit consectetur</h3>
  <p class="pz-body pz-left" style="left:61px;top:411px">Sed ut perspiciatis unde omnis iste natus error sit voluptatem accusantium doloremque laudantium, totam rem aperiam, eaque</p>
  <h3 class="pz-head" style="left:651px;top:184px">Lorem ipsum dolor sit consectetur</h3>
  <p class="pz-body" style="left:651px;top:211px">Sed ut perspiciatis unde omnis iste natus error sit voluptatem accusantium doloremque laudantium, totam rem aperiam, eaque</p>
  <h3 class="pz-head" style="left:651px;top:363px">Lorem ipsum dolor sit consectetur</h3>
  <p class="pz-body" style="left:651px;top:390px">Sed ut perspiciatis unde omnis iste natus error sit voluptatem accusantium doloremque laudantium, totam rem aperiam, eaque</p>
</section>

<!-- Growth chart -->
<section class="slide growth">
  <svg class="abs" width="981" height="552" style="left:0;top:0" font-family="Roboto, Arial, sans-serif">
    <path d="M185,0 H981 V552 H350 C245,552 185,480 185,370 Z" fill="var(--white)"/>
    <g font-size="11" fill="#333" text-anchor="end">
      <text x="248" y="113">120</text><text x="248" y="169">100</text>
      <text x="248" y="224">80</text><text x="248" y="280">60</text>
      <text x="248" y="336">40</text><text x="248" y="381">20</text><text x="248" y="440">0</text>
    </g>
    <g stroke="var(--grid)" stroke-width="1">
      <path d="M257,109 V436 M331,109 V436 M406,109 V436 M480,109 V436 M555,109 V436 M629,109 V436"/>
      <path d="M257,436 H629"/>
    </g>
    <g fill="var(--green)">
      <rect x="278" y="163" width="14" height="273"/>
      <rect x="352" y="191" width="14" height="245"/>
      <rect x="427" y="300" width="14" height="136"/>
      <rect x="501" y="163" width="14" height="273"/>
      <rect x="576" y="163" width="14" height="273"/>
    </g>
    <g fill="var(--navy)">
      <rect x="299" y="191" width="14" height="245"/>
      <rect x="373" y="218" width="14" height="218"/>
      <rect x="448" y="163" width="14" height="273"/>
      <rect x="522" y="272" width="14" height="164"/>
      <rect x="597" y="191" width="14" height="245"/>
    </g>
    <g font-size="11" font-weight="700" fill="#333" text-anchor="middle">
      <text x="285" y="158">100</text><text x="306" y="186">90</text>
      <text x="359" y="186">90</text><text x="380" y="213">80</text>
      <text x="434" y="295">50</text><text x="455" y="158">100</text>
      <text x="508" y="158">100</text><text x="529" y="267">60</text>
      <text x="583" y="158">100</text><text x="604" y="186">90</text>
      <text x="295" y="459">Sun</text><text x="369" y="459">Mon</text>
      <text x="443" y="459">Tue</text><text x="518" y="459">Wed</text><text x="592" y="459">Thu</text>
    </g>
  </svg>
  <h2 class="growth-title">Growth</h2>
  <div class="growth-rule"></div>
  <ul class="growth-list">
    <li><svg class="tick" viewBox="0 0 12 12"><circle cx="6" cy="6" r="6" fill="var(--green)"/><path d="M3.2 6.2 L5.2 8 L8.8 4.2" stroke="#fff" stroke-width="1.5" fill="none"/></svg>Lorem ipsum sit consectetur adipiscing elit, sed do eiusmod tempor incididunt ut labore et aliqua.</li>
    <li><svg class="tick" viewBox="0 0 12 12"><circle cx="6" cy="6" r="6" fill="var(--green)"/><path d="M3.2 6.2 L5.2 8 L8.8 4.2" stroke="#fff" stroke-width="1.5" fill="none"/></svg>Lorem ipsum sit consectetur adipiscing elit, sed do eiusmod tempor incididunt ut labore et aliqua.</li>
    <li><svg class="tick" viewBox="0 0 12 12"><circle cx="6" cy="6" r="6" fill="var(--green)"/><path d="M3.2 6.2 L5.2 8 L8.8 4.2" stroke="#fff" stroke-width="1.5" fill="none"/></svg>Lorem ipsum sit consectetur adipiscing elit, sed do eiusmod tempor incididunt ut labore et aliqua.</li>
    <li><svg class="tick" viewBox="0 0 12 12"><circle cx="6" cy="6" r="6" fill="var(--green)"/><path d="M3.2 6.2 L5.2 8 L8.8 4.2" stroke="#fff" stroke-width="1.5" fill="none"/></svg>Lorem ipsum sit consectetur adipiscing elit, sed do eiusmod tempor incididunt ut labore et aliqua.</li>
    <li><svg class="tick" viewBox="0 0 12 12"><circle cx="6" cy="6" r="6" fill="var(--green)"/><path d="M3.2 6.2 L5.2 8 L8.8 4.2" stroke="#fff" stroke-width="1.5" fill="none"/></svg>Lorem ipsum sit consectetur adipiscing elit, sed do eiusmod tempor incididunt ut labore et aliqua.</li>
    <li><svg class="tick" viewBox="0 0 12 12"><circle cx="6" cy="6" r="6" fill="var(--green)"/><path d="M3.2 6.2 L5.2 8 L8.8 4.2" stroke="#fff" stroke-width="1.5" fill="none"/></svg>Lorem ipsum sit consectetur adipiscing elit, sed do eiusmod tempor incididunt ut labore et aliqua.</li>
  </ul>
</section>

<!-- Closing -->
<section class="slide closing">
  <div class="photo" role="img" aria-label="Smiling support agent wearing a headset in a bright office" style="clip-path:path('M0,0 H456 C380,120 380,300 440,400 C480,470 510,520 515,552 H0 Z')"></div>
  <div class="brand on-white" style="left:704px;top:43px"><span class="brand-dot"></span><span class="brand-name">MedoraVix</span></div>
  <div class="thanks-dash"><span></span><span></span><span></span></div>
  <h2 class="thanks">THANK YOU</h2>
  <p class="presenter">Presenter Name</p>
  <p class="contact" style="top:367px"><svg viewBox="0 0 28 28"><path d="M7 4 L11 4 L13 10 L10 12 C11.5 15.5 13 17 16 18.5 L18 15.5 L24 17.5 L24 21.5 C24 23 22.5 24 21 24 C12 23 5 16 4 7 C4 5.5 5.5 4 7 4 Z" fill="var(--green)"/></svg>+1 (888) 888 8888</p>
  <p class="contact" style="top:409px"><svg viewBox="0 0 28 28" fill="none" stroke="var(--green)" stroke-width="2"><circle cx="14" cy="14" r="10"/><ellipse cx="14" cy="14" rx="4.5" ry="10"/><path d="M4 14 H24 M6 9 H22 M6 19 H22"/></svg>www.yourwebsite.com</p>
  <p class="contact" style="top:452px"><svg viewBox="0 0 28 28"><rect x="3" y="7" width="22" height="15" fill="var(--green)"/><path d="M3 7 L14 16 L25 7" stroke="#fff" stroke-width="1.6" fill="none"/></svg>info@medoravix.com</p>
  <p class="contact" style="top:493px"><svg viewBox="0 0 28 28"><path d="M14 3 C9 3 6 6.5 6 11 C6 17 14 25 14 25 C14 25 22 17 22 11 C22 6.5 19 3 14 3 Z" fill="var(--green)"/><circle cx="14" cy="11" r="3.2" fill="#fff"/></svg>Add your Location here</p>
</section>

</body>
</html>
```